Heron Ridge Distillery Bottle Label Design

We need a label design for a product called "Cedar Hollow Straight Bourbon Whiskey". The bottle has two embossments on the side and an image printed on the back that will show through when looking from the front (shown in the attached image). It's made of 30% rye and 70% corn; images of the ingredients can be incorporated into the label design. We are a distillery that produces whiskey and bourbon from local farmers around the area. We focus on the quality of the ingredients and using the recipes passed down from generation to generation. We like a straight forward design using two colors maximum. The background will be brown once filled with the bourbon, so it must contrast against it (i.e. white and other lighter colors). The Heron Ridge Distillery logo must be present on the bottle front, as well as 750 ml, 84 PROOF, 42% ALC/VOL.

Target Market(s)

Craft whiskey consumers.

Industry/Entity Type

Product

Colors
fee18a
fbe7d2
fff3d1
fefcee
fefdec
fdf9cf

Requirements
Must have
• 750 ml, 84 PROOF, 42% ALC/VOL. Aged for 3 years.The Heron Ridge Distillery logo must be present on the bottle. Only two colors on label.
Nice to have
• Story of how we are a micro distillery making hand crafted whiskey.
Should not have
• False or misleading print.

```html
<!DOCTYPE html>
<html lang="en">
<head>
<meta charset="utf-8">
<title>Cedar Hollow Straight Bourbon Whiskey — Label</title>
<link rel="stylesheet" href="https://fonts.googleapis.com/css2?family=Rye&family=Pinyon+Script&family=Cormorant+Garamond:ital,wght@1,600&family=Special+Elite&family=Cinzel:wght@700&display=swap">
<style>
  :root {
    --backdrop: #1a120c;
    --paper: #f3ead6;
    --paper-light: #fbf4e4;
    --ink: #5a3a22;
    --ink-soft: #8a6a4c;
    --band: #4a2e1c;
  }
  * { margin: 0; padding: 0; box-sizing: border-box; }
  html, body {
    width: 741px; height: 1200px; overflow: hidden;
    background: var(--backdrop);
  }
  .label {
    position: absolute; left: 30px; top: 218px;
    width: 681px; height: 764px;
    color: var(--ink);
  }
  .label-frame { position: absolute; inset: 0; }
  .brand {
    position: absolute; left: 230px; width: 221px; top: 58px;
    display: flex; flex-direction: column; align-items: center; gap: 8px;
  }
  .brand-dot { width: 38px; height: 38px; border-radius: 50%; background: var(--ink); }
  .brand-name {
    font-family: "Cinzel", serif; font-weight: 700; font-size: 17px;
    line-height: 1.2; letter-spacing: 1px; color: var(--ink); text-align: center;
  }
  .tag {
    position: absolute; top: 128px; height: 44px;
    border: 2px solid var(--ink);
    display: flex; align-items: center; justify-content: center;
    font-family: "Cormorant Garamond", serif; font-style: italic; font-weight: 600;
    font-size: 20px; color: var(--ink); white-space: nowrap;
  }
  .tag-left { left: 40px; width: 170px; }
  .tag-right { right: 40px; width: 190px; font-size: 17px; }
  .title-frame { position: absolute; left: 60px; top: 215px; width: 500px; height: 215px; }
  .title {
    position: absolute; left: 100px; top: 262px; width: 440px;
    font-family: "Rye", serif; font-weight: 400; font-size: 46px; line-height: 1.15;
    color: var(--ink); text-shadow: 2px 2px 0 var(--ink-soft); white-space: nowrap;
  }
  .title-line { display: block; }
  .title-line.indent { padding-left: 120px; }
  .flourish {
    position: absolute;
    background: linear-gradient(90deg, rgba(138,106,76,.35), rgba(138,106,76,.15));
    border-radius: 40px;
  }
  .flourish-top { left: 440px; top: 210px; width: 180px; height: 70px; }
  .flourish-bottom { left: 80px; top: 360px; width: 150px; height: 60px; }
  .band {
    position: absolute; left: 0; right: 0; top: 470px; height: 46px;
    background: var(--band);
  }
  .band-plate {
    position: absolute; left: 70px; top: 456px; width: 310px; height: 72px;
    background: var(--paper-light); border: 2px solid var(--ink); border-radius: 8px;
    display: flex; align-items: center; justify-content: center;
    font-family: "Pinyon Script", cursive; font-size: 40px; color: var(--ink);
  }
  .specs {
    position: absolute; left: 0; right: 0; top: 588px;
    text-align: center; color: var(--ink);
  }
  .specs-aged { font-family: "Cormorant Garamond", serif; font-style: italic; font-weight: 600; font-size: 28px; }
  .specs-line { font-family: "Special Elite", monospace; font-size: 24px; margin-top: 8px; }
  .specs-volume { font-family: "Cormorant Garamond", serif; font-style: italic; font-weight: 600; font-size: 28px; margin-top: 14px; }
  .grain-art {
    position: absolute; top: 560px; width: 180px; height: 170px;
    background: radial-gradient(ellipse at center, rgba(138,106,76,.45), rgba(138,106,76,.1) 70%);
  }
  .grain-left { left: 36px; }
  .grain-right { right: 36px; }
</style>
</head>
<body>
  <section class="label">
    <svg class="label-frame" viewBox="0 0 681 764" aria-hidden="true">
      <path d="M40 0 H641 A40 40 0 0 0 681 40 V724 A40 40 0 0 0 641 764 H40 A40 40 0 0 0 0 724 V40 A40 40 0 0 0 40 0 Z" fill="#f3ead6"/>
      <path d="M52 14 H629 A38 38 0 0 0 667 52 V712 A38 38 0 0 0 629 750 H52 A38 38 0 0 0 14 712 V52 A38 38 0 0 0 52 14 Z" fill="none" stroke="#5a3a22" stroke-width="3"/>
      <path d="M60 22 H621 A38 38 0 0 0 659 60 V704 A38 38 0 0 0 621 742 H60 A38 38 0 0 0 22 704 V60 A38 38 0 0 0 60 22 Z" fill="none" stroke="#5a3a22" stroke-width="1.2"/>
    </svg>

    <div class="brand">
      <span class="brand-dot"></span>
      <span class="brand-name">Heron Ridge<br>Distillery</span>
    </div>

    <div class="tag tag-left">hand crafted</div>
    <div class="tag tag-right">30% rye and 70% corn</div>

    <svg class="title-frame" viewBox="0 0 500 215" aria-hidden="true">
      <path d="M20 2 H480 A18 18 0 0 0 498 20 V195 A18 18 0 0 0 480 213 H20 A18 18 0 0 0 2 195 V20 A18 18 0 0 0 20 2 Z" fill="none" stroke="#5a3a22" stroke-width="3"/>
    </svg>
    <div class="flourish flourish-top" role="img" aria-label="Engraved scrollwork flourish"></div>
    <div class="flourish flourish-bottom" role="img" aria-label="Engraved scrollwork flourish"></div>

    <h1 class="title">
      <span class="title-line">CEDAR HOLLOW</span>
      <span class="title-line indent">STRAIGHT</span>
    </h1>

    <div class="band"></div>
    <div class="band-plate">Bourbon Whiskey</div>

    <div class="grain-art grain-left" role="img" aria-label="Engraved illustration of rye and corn sheaves"></div>
    <div class="grain-art grain-right" role="img" aria-label="Engraved illustration of rye and corn sheaves"></div>

    <div class="specs">
      <p class="specs-aged">aged for 3 years</p>
      <p class="specs-line">84 PROOF,</p>
      <p class="specs-line">42% ALC/VOL.</p>
      <p class="specs-volume">750 ml</p>
    </div>
  </section>
</body>
</html>
```